Wordpress site for cyber security and network perfomance software vendor

We need a brand new Wordpress website consisting of a single home/landing page and page template so that we can add pages in future.
The website is intended to provide information to prospects and customers. The homepage should have a top menu bar that is customizable similar to what we already have at qelvora.com.
Note that we are after a new design – that is, please don’t reference our existing website for design inspiration (qelvora.com)
We are after a Wordpress site that may be implemented straight onto our Wordpress hoster (HostMarrow) .
Quillmo is a software company delivering a solution for customers to get visibility of network performance and cyber security. The Quillmo solution reduces cyber security risk, identifies performance bottlenecks and ultimately lower costs by reducing the number of tools need to monitor the IT environment
We deliver network performance and cyber security information to the IT manager and network teams in a format that they understand, at a realistic cost, and requiring minimal resource to implement. This is a crowded market, most competitors provide highly complex, expensive and highly customized tools to large enterprise. Quillmo makes this style of visibility tool accessible to the mid market.

Target Market(s)

IT Managers, network engineers, mid market organisations, IT service providers

Industry/Entity Type

IT

Font styles to use
Sans Serif

Colors
0094D4
00A9DD
6FCCEA
C7EBF8
E9F6FB

Requirements
Must have
• Fully coded for WordPress. Responsive and mobile friendly. The website copy is provided in the attached document. Utilise the Quillmo logo colors as part of the design (Dark Blue: 2E4F99, Light Blue: 00AFF4, Green: 73D94F). Top Horizontal menu bar for additional pages. Implement one of our screenshots (I have included a bunch of screenshots to choose from)
Nice to have
• Icons, panels or infographics matching the services. Our existing site is built using Pelk – this is not a requirement for the new site but a nice to have as we are familiar with Pelk.
Should not have
• Preferably no corporate images – business people shaking hands or teams of people a meeting room (or that kind of thing)

```html
<!DOCTYPE html>
<html lang="en">
<head>
<meta charset="utf-8">
<title>Quillmo – Security + Visibility</title>
<link href="https://fonts.googleapis.com/css2?family=Barlow:ital,wght@0,500;0,600;0,700;1,400&family=Roboto:ital,wght@0,400;0,500;1,400&display=swap" rel="stylesheet">
<style>
:root{
  --navy:#0f1a35;
  --brand-blue:#2E4F99;
  --sky:#00AFF4;
  --cyan:#00A9DD;
  --green:#73D94F;
  --lime:#8fd13f;
  --teal:#1fb8c2;
  --lavender:#eef1fb;
  --text:#5a6070;
  --white:#ffffff;
}
*{margin:0;padding:0;box-sizing:border-box}
html,body{width:1200px;height:4874px;overflow:hidden}
body{font-family:"Roboto",Arial,sans-serif;color:var(--text);background:var(--white)}
.page{position:relative;width:1200px;height:4874px;overflow:hidden}
.abs{position:absolute}
.bg-svg{position:absolute;left:0;display:block}
h1,h2,h3,.display{font-family:"Barlow",Arial,sans-serif}
.btn{position:absolute;display:flex;align-items:center;justify-content:center;border-radius:22px;color:var(--white);font-family:"Barlow",Arial,sans-serif;font-weight:600;font-size:15px;letter-spacing:.3px;text-decoration:none}
.btn-grad{background:linear-gradient(90deg,var(--cyan),var(--green))}
.btn-navy{background:var(--brand-blue)}
.ph{position:absolute}

/* header */
.brand{position:absolute;left:60px;top:20px;display:flex;align-items:center;gap:10px;font-family:"Barlow",Arial,sans-serif;font-weight:600;font-size:32px;color:var(--brand-blue)}
.brand-dot{width:34px;height:34px;border-radius:50%;background:var(--sky)}
.nav{position:absolute;left:645px;top:30px;display:flex;font-family:"Barlow",Arial,sans-serif;font-size:13px;font-weight:500;color:var(--navy)}
.nav a{color:var(--navy);text-decoration:none;margin-right:22px}
.nav a.active{color:var(--lime)}

/* hero */
.hero-title{position:absolute;left:112px;top:222px;font-size:66px;line-height:68px;font-weight:700;color:var(--navy);letter-spacing:1px}
.hero-title .plus{color:var(--sky)}
.hero-title .green{color:var(--lime)}
.hero-sub{position:absolute;left:114px;top:366px;font-size:15px;color:#333}

/* intro */
.intro-title{position:absolute;left:200px;width:800px;top:740px;text-align:center;font-size:33px;line-height:44px;font-weight:600;color:var(--brand-blue)}
.intro-title .accent{color:var(--sky)}
.intro-copy{position:absolute;left:290px;width:620px;top:895px;text-align:center;font-size:12.5px;line-height:19.5px;color:#555}
.intro-copy p{margin-bottom:13px}

/* why */
.sec-title{position:absolute;font-size:35px;line-height:38px;font-weight:700;color:var(--brand-blue)}
.sec-title .accent{color:var(--sky)}
.why-copy{position:absolute;left:142px;top:1342px;width:394px;font-size:11.5px;line-height:19.5px;color:#666}
.why-copy p{margin-bottom:11px}
.why-copy .lead-blue{color:var(--brand-blue);font-style:italic;font-size:14px;margin-bottom:14px}
.why-copy .lead-green{color:var(--lime);font-style:italic;font-size:14px}

/* services */
.svc-heading{position:absolute;left:300px;width:600px;top:1886px;text-align:center;font-size:33px;line-height:42px;font-weight:600}
.svc-heading .l1{color:#2f5fb8}
.svc-heading .l2{color:var(--white)}
.svc{position:absolute;width:270px;text-align:center}
.svc svg{display:block;margin:0 auto}
.svc h3{font-family:"Roboto",Arial,sans-serif;font-weight:400;font-size:15px;line-height:20px;color:#2f74c8;margin-top:22px}
.svc p{font-size:11.5px;line-height:19.5px;color:#cdd3e2;margin-top:8px}

/* committed */
.commit-text{position:absolute;left:738px;top:2822px;width:440px;font-family:"Barlow",Arial,sans-serif;font-weight:600;font-size:23px;line-height:34px;color:var(--white);white-space:nowrap}

/* range */
.range-box{position:absolute;left:292px;top:3215px;width:616px;height:170px;border:2px solid var(--brand-blue);border-radius:20px}
.range-text{position:absolute;left:292px;width:616px;top:3282px;text-align:center;font-family:"Barlow",Arial,sans-serif;font-weight:600;font-size:21px;line-height:32px;color:var(--navy)}
.dot{position:absolute;width:12px;height:12px;border-radius:50%;background:var(--brand-blue)}

/* no obligation */
.obl-copy{position:absolute;left:124px;top:3632px;width:380px;font-size:12px;line-height:21px;color:#666}
.steps{position:absolute;left:124px;top:3762px;list-style:none;font-size:12px;color:#333}
.steps li{display:flex;align-items:center;height:29px}
.steps svg{margin-right:14px}

/* contact */
.contact-title{position:absolute;left:168px;top:4264px;font-size:33px;line-height:40px;font-weight:700;color:var(--brand-blue)}
.field{position:absolute;left:632px;width:348px;height:36px;border-radius:6px;background:rgba(255,255,255,.28);color:var(--white);font-size:11px;padding:10px 14px}

/* footer */
.foot-brand{position:absolute;left:64px;top:4598px;display:flex;align-items:center;gap:14px;font-family:"Barlow",Arial,sans-serif;font-weight:600;font-size:46px;color:#3d7fd6}
.foot-brand .brand-dot{width:52px;height:52px}
.foot-mail{position:absolute;left:116px;top:4722px;display:flex;align-items:center;gap:10px;color:var(--white);font-size:13px}
.foot-col{position:absolute;top:4606px;font-size:11px;color:#d6dbe8}
.foot-col h4{font-family:"Roboto",Arial,sans-serif;font-weight:400;font-size:15px;color:#2f74c8;margin-bottom:20px}
.foot-col ul{list-style:none}
.foot-col li{height:24.5px;display:flex;align-items:center}
.foot-col li::before{content:"";width:4px;height:4px;border-radius:50%;background:var(--lime);margin-right:20px}
.addr{display:flex;gap:16px;line-height:18px;margin-bottom:24px}
.copyright{position:absolute;left:0;width:1200px;top:4846px;text-align:center;font-size:11px;color:#d6dbe8}
.copyright span{color:var(--sky)}
</style>
</head>
<body>
<div class="page">

  <!-- HERO BACKGROUND -->
  <svg class="bg-svg" style="top:0" width="1200" height="1320" viewBox="0 0 1200 1320">
    <path d="M0 710 C120 640 200 690 330 680 C480 670 580 610 760 640 C930 665 1080 690 1200 640 L1200 1320 L0 1320 Z" fill="var(--lavender)"/>
    <path d="M0 700 C40 610 140 590 250 600 C360 610 450 560 560 590 C440 590 330 640 220 640 C120 640 50 660 0 720 Z" fill="var(--lime)"/>
    <path d="M960 150 C1000 100 1080 100 1120 130 C1160 160 1200 140 1200 140 L1200 690 C1150 700 1100 640 1120 590 C1030 560 980 470 1000 380 C1020 280 930 230 960 150 Z" fill="var(--lime)"/>
    <path d="M0 1200 C200 1300 400 1230 560 1250 C700 1270 760 1330 900 1300 C1040 1270 1120 1230 1200 1250 L1200 1320 L0 1320 Z" fill="var(--white)"/>
  </svg>

  <!-- HEADER -->
  <div class="brand"><span class="brand-dot"></span>Quillmo</div>
  <nav class="nav">
    <a class="active" href="#">HOME</a><a href="#">PRODUCTS</a><a href="#">BLOG</a><a href="#">ABOUT</a><a href="#">PARTNER PORTAL</a>
  </nav>
  <a class="btn btn-grad" href="#" style="left:1012px;top:20px;width:130px;height:38px;">DEMO LOGIN</a>

  <!-- HERO -->
  <h1 class="hero-title">SECURITY <span class="plus">+</span><br><span class="green">VISIBILITY</span></h1>
  <p class="hero-sub">Network monitoring for IT Performance and Security</p>
  <a class="btn btn-grad" href="#" style="left:112px;top:403px;width:136px;height:38px;">GO TO DEMO</a>
  <div class="ph" role="img" aria-label="Quillmo network performance dashboard screenshot with traffic graph and donut charts" style="left:588px;top:190px;width:560px;height:350px;background:linear-gradient(160deg,#2a2e36,#15171c);border:8px solid #e9eaee;border-radius:10px 10px 0 0;"></div>
  <div class="ph" style="left:500px;top:556px;width:700px;height:14px;background:#dfe1e6;border-radius:0 0 14px 14px"></div>

  <!-- INTRO -->
  <h2 class="intro-title">Specialising in IT Network Performance and<br>Cyber Security Solutions for Small to<br><span class="accent">Medium Organisations.</span></h2>
  <div class="intro-copy">
    <p>Do you feel concerned about your network performance, and cyber threats, but you don't have the time or staff to deal with it?</p>
    <p>Perhaps you've outsourced your IT support and have discovered that your service provider doesn't have visibility of you network?</p>
    <p>It's not easy being an IT manager. Especially if you work in a small to medium sized organisation. You're typically stretched to the limit with an understaffed team and there's simply not enough hours in the day to tackle all the increasing demands.</p>
  </div>
  <a class="btn btn-grad" href="#" style="left:529px;top:1080px;width:142px;height:38px;">LEARN MORE</a>

  <!-- WHY -->
  <h2 class="sec-title" style="left:140px;top:1248px;">WHY<br><span class="accent">QUILLMO?</span></h2>
  <div class="why-copy">
    <p>At Quillmo, we understand the challenges that you face. Cyber security and network incidents can have devastating impacts on small to medium organisations because you typically don't have the time, staff, or resources to develop complicated responses to cyber security threats.</p>
    <p>That's why small to medium sized organisations are vulnerable to potentially devastating cyber incidents. Did you know that on average, it took over 220 days for organisations to identify a breach and a further 80 days to contain the breach? (Norvane Research, 2020).</p>
    <p class="lead-blue">With Quillmo, you can avoid these unpleasant surprises.</p>
    <p>We're committed to providing the best easy-to-use cyber tools for small to medium organisations that will give you visibility across your network, performance, AND cyber security data. So, you won't get any nasty surprises.</p>
    <p class="lead-green">Network engineers love our easy-to-use tools, and you will too!</p>
  </div>
  <div class="ph" role="img" aria-label="Network engineer at work seen through a circular connected-node shape with code overlays" style="left:650px;top:1290px;width:390px;height:390px;border-radius:50%;background:radial-gradient(circle at 45% 45%,#c9b7a6 0%,#6b6f7a 45%,#1d2435 100%);"></div>

  <!-- SERVICES DARK SECTION -->
  <svg class="bg-svg" style="top:1740px" width="1200" height="900" viewBox="0 0 1200 900">
    <path d="M0 40 C160 20 300 90 450 70 C590 50 640 -10 760 20 C900 55 1040 50 1200 10 L1200 900 L0 900 Z" fill="var(--lime)"/>
    <path d="M0 52 C160 34 300 104 450 84 C590 64 640 6 760 36 C900 70 1040 66 1200 28 L1200 900 L0 900 Z" fill="var(--navy)"/>
  </svg>
  <h2 class="svc-heading"><span class="l1">WE DELIVER EVERYTHING</span><br><span class="l2">YOU NEED</span></h2>

  <div class="svc" style="left:168px;top:2015px;">
    <svg width="90" height="84" viewBox="0 0 90 84"><circle cx="52" cy="44" r="36" fill="#1c2846"/><rect x="18" y="10" width="44" height="52" fill="none" stroke="var(--lime)" stroke-width="2.5"/><path d="M24 48 L34 36 L42 42 L54 24" fill="none" stroke="var(--sky)" stroke-width="2.5"/><circle cx="58" cy="50" r="14" fill="none" stroke="var(--sky)" stroke-width="2.5"/><path d="M58 36 V50 H72" fill="none" stroke="var(--lime)" stroke-width="2.5"/></svg>
    <h3>Sophisticated Data Analytics</h3>
    <p>Powerful data analytics correlate threat data and anomalous traffic flows with network performance to deliver meaningful information so you can easily respond.</p>
  </div>
  <div class="svc" style="left:465px;top:2015px;">
    <svg width="90" height="84" viewBox="0 0 90 84"><circle cx="52" cy="44" r="36" fill="#1c2846"/><rect x="20" y="10" width="48" height="54" fill="none" stroke="var(--lime)" stroke-width="2.5"/><rect x="28" y="40" width="7" height="18" fill="var(--sky)"/><rect x="39" y="30" width="7" height="28" fill="var(--sky)"/><rect x="50" y="20" width="7" height="38" fill="var(--sky)"/></svg>
    <h3>Best Visual Analytics</h3>
    <p>Proactive alerts and dynamic traffic flows are integrated into an intuitive, user friendly dashboard that enable you to plug your visibility blind spots.</p>
  </div>
  <div class="svc" style="left:758px;top:2015px;">
    <svg width="90" height="84" viewBox="0 0 90 84"><circle cx="52" cy="44" r="36" fill="#1c2846"/><circle cx="44" cy="40" r="26" fill="none" stroke="var(--lime)" stroke-width="2.5" stroke-dasharray="6 4"/><path d="M32 34 L38 26 H50 L56 34 L44 52 Z" fill="none" stroke="var(--sky)" stroke-width="2.5"/><path d="M32 34 H56" stroke="var(--sky)" stroke-width="2"/></svg>
    <h3>Superior Service</h3>
    <p>From first contact through to deployment, our friendly, expert team will discuss your needs and quickly install our easy-to-use platform and tools.</p>
  </div>
  <div class="svc" style="left:168px;top:2300px;">
    <svg width="90" height="84" viewBox="0 0 90 84"><circle cx="52" cy="44" r="36" fill="#1c2846"/><circle cx="44" cy="40" r="20" fill="none" stroke="var(--lime)" stroke-width="7" stroke-dasharray="5 5"/><circle cx="44" cy="40" r="13" fill="#1c2846" stroke="var(--lime)" stroke-width="2.5"/><path d="M37 40 L42 45 L51 35" fill="none" stroke="var(--sky)" stroke-width="2.5"/></svg>
    <h3>Flexible Solutions</h3>
    <p>Our network monitoring AND cyber security solution can be scaled to fit your organisation.</p>
  </div>
  <div class="svc" style="left:465px;top:2300px;">
    <svg width="90" height="84" viewBox="0 0 90 84"><circle cx="52" cy="44" r="36" fill="#1c2846"/><path d="M36 12 H52 L47 22 H41 Z" fill="none" stroke="var(--lime)" stroke-width="2.5"/><path d="M41 22 C24 32 22 60 44 60 C66 60 64 32 47 22" fill="none" stroke="var(--lime)" stroke-width="2.5"/><text x="44" y="50" text-anchor="middle" font-family="Roboto,sans-serif" font-size="16" fill="var(--sky)">$</text><path d="M14 66 H70" stroke="var(--sky)" stroke-width="2.5"/></svg>
    <h3>Decrease your total cost of<br>Ownership</h3>
    <p>The Quillmo platform will give you visibility across your network performance AND cyber security data. YOU WON'T NEED additional tools, add-ons, or specialised training.</p>
  </div>
  <svg class="abs" style="left:750px;top:2250px" width="370" height="270" viewBox="0 0 370 270">
    <path d="M8 240 C60 260 100 250 130 200 C160 150 190 150 240 140 C300 128 330 80 350 30" fill="none" stroke="#9aa6c0" stroke-width="1.5" stroke-dasharray="3 4"/>
    <path d="M314 38 L360 16 L352 64 L342 44 Z" fill="var(--lime)"/>
  </svg>

  <!-- COMMITTED GRADIENT BAND -->
  <svg class="bg-svg" style="top:2530px" width="1200" height="600" viewBox="0 0 1200 600">
    <defs>
      <linearGradient id="bandGrad" x1="0" y1="0" x2="1" y2="0">
        <stop offset="0" stop-color="#94d34a"/>
        <stop offset=".5" stop-color="#22bcb8"/>
        <stop offset="1" stop-color="#1e8ad8"/>
      </linearGradient>
    </defs>
    <path d="M0 240 C140 200 260 300 420 250 C560 205 600 120 760 120 C900 120 960 20 1080 10 C1150 5 1190 30 1200 40 L1200 560 C1100 600 1000 540 880 560 C740 585 640 520 520 560 C400 600 330 560 200 560 C120 560 60 600 0 580 Z" fill="url(#bandGrad)"/>
  </svg>
  <div class="ph" role="img" aria-label="Excited man in a white shirt pointing at a laptop" style="left:70px;top:2620px;width:380px;height:490px;border-radius:160px 160px 0 0;background:linear-gradient(180deg,#c99a7a 0%,#e9e6e2 35%,#f5f5f3 100%);"></div>
  <div class="ph" role="img" aria-label="Laptop showing the Quillmo dashboard" style="left:410px;top:2848px;width:240px;height:160px;background:linear-gradient(160deg,#2b2f38,#14161b);border:6px solid #e4e6ea;border-radius:8px 8px 0 0;"></div>
  <div class="ph" style="left:380px;top:3008px;width:300px;height:14px;background:#d9dce2;border-radius:0 0 12px 12px"></div>
  <p class="commit-text">At Quillmo, We're Committed To<br>Providing You The Best Easy-To-Use<br>Tools That Will Give You Visibility,<br>Security, And Peace Of Mind.</p>
  <a class="btn btn-navy" href="#" style="left:738px;top:2975px;width:142px;height:38px;">CONTACT US</a>

  <!-- RANGE -->
  <div class="range-box"></div>
  <span class="dot" style="left:499px;top:3209px"></span>
  <span class="dot" style="left:688px;top:3209px"></span>
  <svg class="abs" style="left:560px;top:3170px;background:var(--white)" width="80" height="84" viewBox="0 0 80 84">
    <path d="M34 8 C30 20 30 40 36 60 L44 70 L56 62 L48 46 L40 48 C38 40 38 28 40 20 L48 22 L54 6 L42 2 Z" fill="var(--lime)"/>
    <path d="M20 40 H50 C56 40 56 48 50 48 H60 C66 48 66 56 60 56 H58 C64 56 64 64 58 64 H28 L20 60 Z" fill="none" stroke="var(--brand-blue)" stroke-width="3"/>
    <rect x="10" y="38" width="12" height="28" fill="var(--brand-blue)"/>
  </svg>
  <p class="range-text">A RANGE OF APPLICATION FOR EVERY<br>REQUIREMENT</p>
  <a class="btn btn-grad" href="#" style="left:518px;top:3366px;width:164px;height:38px;">GIVE US A CALL!</a>

  <!-- NO OBLIGATION -->
  <h2 class="sec-title" style="left:120px;top:3540px;">NO<br><span class="accent">OBLIGATION.</span></h2>
  <p class="obl-copy">All information is sent to the central cloud based reporting server for analysis and presentation. Simply log in to your account on the Quillmo cloud based server to view you gauge what your users are experiencing or assess your current cyber security posture.</p>
  <ul class="steps">
    <li><svg width="28" height="10" viewBox="0 0 28 10"><path d="M0 5 H26 M20 1 L26 5 L20 9" fill="none" stroke="var(--lime)" stroke-width="1.6"/></svg>Answer 2-3 Questions</li>
    <li><svg width="28" height="10" viewBox="0 0 28 10"><path d="M0 5 H26 M20 1 L26 5 L20 9" fill="none" stroke="var(--lime)" stroke-width="1.6"/></svg>Give us your name and email to send your our findings</li>
    <li><svg width="28" height="10" viewBox="0 0 28 10"><path d="M0 5 H26 M20 1 L26 5 L20 9" fill="none" stroke="var(--lime)" stroke-width="1.6"/></svg>In a few Days, we will send you a customized website evaluation</li>
    <li><svg width="28" height="10" viewBox="0 0 28 10"><path d="M0 5 H26 M20 1 L26 5 L20 9" fill="none" stroke="var(--lime)" stroke-width="1.6"/></svg>That's it! No obligation on your part!</li>
  </ul>
  <a class="btn btn-grad" href="#" style="left:120px;top:3900px;width:240px;height:38px;">GET YOUR FREE EVOLUTION</a>
  <svg class="abs" style="left:580px;top:3480px" width="520" height="480" viewBox="0 0 520 480">
    <path d="M20 160 C-10 300 80 420 230 440" fill="none" stroke="var(--lime)" stroke-width="1.5" stroke-dasharray="3 4"/>
  </svg>
  <div class="ph" role="img" aria-label="Engineers inspecting server racks in a data centre" style="left:596px;top:3490px;width:320px;height:320px;border-radius:50%;background:radial-gradient(circle at 60% 50%,#b9c4d6 0%,#4c5a74 45%,#141c2c 100%);"></div>
  <div class="ph" role="img" aria-label="Glowing blue padlock over a circuit background" style="left:810px;top:3690px;width:280px;height:260px;border-radius:50%;background:radial-gradient(circle at 50% 45%,#3c8ff0 0%,#16448f 45%,#07152f 100%);"></div>
  <svg class="abs" style="left:800px;top:3900px" width="50" height="34" viewBox="0 0 50 34"><path d="M2 30 L48 4 L30 32 L24 20 Z" fill="none" stroke="var(--lime)" stroke-width="1.5"/></svg>

  <!-- CONTACT -->
  <svg class="bg-svg" style="top:4010px" width="1200" height="864" viewBox="0 0 1200 864">
    <defs>
      <linearGradient id="contactGrad" x1="0" y1="0" x2="1" y2="0">
        <stop offset="0" stop-color="#94d34a"/>
        <stop offset=".55" stop-color="#22bcb8"/>
        <stop offset="1" stop-color="#2a8fd6"/>
      </linearGradient>
    </defs>
    <path d="M0 230 C120 210 220 150 340 90 C460 30 560 40 680 120 C800 200 900 110 1020 60 C1110 25 1170 40 1200 50 L1200 620 L0 620 Z" fill="url(#contactGrad)"/>
    <path d="M0 520 C140 560 300 480 440 490 C560 500 620 560 760 540 C900 520 960 450 1080 470 C1150 480 1190 500 1200 510 L1200 864 L0 864 Z" fill="var(--navy)"/>
  </svg>
  <h2 class="contact-title">WE WOULD LOVE TO<br>HEAR FROM YOU.</h2>
  <div class="field" style="top:4194px">Name *</div>
  <div class="field" style="top:4240px">Email *</div>
  <div class="field" style="top:4286px">Phone *</div>
  <div class="field" style="top:4330px;height:72px">Message *</div>
  <a class="btn btn-navy" href="#" style="left:864px;top:4408px;width:112px;height:38px;">SUBMIT</a>

  <!-- FOOTER -->
  <div class="foot-brand"><span class="brand-dot"></span>Quillmo</div>
  <div class="foot-mail">
    <svg width="16" height="12" viewBox="0 0 16 12"><rect x="1" y="1" width="14" height="10" fill="none" stroke="var(--sky)" stroke-width="1.5"/><path d="M1 1 L8 7 L15 1" fill="none" stroke="var(--sky)" stroke-width="1.5"/></svg>
    info@qelvora.com
  </div>
  <div class="foot-col" style="left:336px">
    <h4>Quillmo Australia</h4>
    <ul><li>Home</li><li>Product</li><li>Blog</li><li>About</li><li>Partner Portal</li><li>Demo Login</li></ul>
  </div>
  <div class="foot-col" style="left:612px">
    <h4>Quillmo Australia</h4>
    <div class="addr"><svg width="18" height="20" viewBox="0 0 18 20"><path d="M9 19 C3 12 2 9 2 7 A7 7 0 0 1 16 7 C16 9 15 12 9 19 Z" fill="var(--lime)"/><circle cx="9" cy="7" r="2.5" fill="var(--navy)"/></svg><span>Level 4, 28 Harbourline Street<br>Pyrmont, NSW, 2009<br>Australia</span></div>
    <div class="addr"><svg width="18" height="18" viewBox="0 0 18 18"><path d="M4 1 L7 5 L5 7 C6 10 8 12 11 13 L13 11 L17 14 L15 17 C8 17 1 10 1 3 Z" fill="var(--lime)"/></svg><span>+61 2 5550 1842</span></div>
  </div>
  <div class="foot-col" style="left:888px">
    <h4>Quillmo Germany</h4>
    <div class="addr"><svg width="18" height="20" viewBox="0 0 18 20"><path d="M9 19 C3 12 2 9 2 7 A7 7 0 0 1 16 7 C16 9 15 12 9 19 Z" fill="var(--lime)"/><circle cx="9" cy="7" r="2.5" fill="var(--navy)"/></svg><span>Level 4, 28 Harbourline Street<br>Pyrmont, NSW, 2009<br>Australia</span></div>
    <div class="addr"><svg width="18" height="18" viewBox="0 0 18 18"><path d="M4 1 L7 5 L5 7 C6 10 8 12 11 13 L13 11 L17 14 L15 17 C8 17 1 10 1 3 Z" fill="var(--lime)"/></svg><span>+49 69 555 40 218</span></div>
  </div>
  <p class="copyright">©<span>Quillmo</span> -2021 All rights reserved.</p>

</div>
</body>
</html>
```